Dental Plan for Dogs

We are a vet clinic and I am wanting a poster designed that can then ultimately be changed/rejigged to be use on a website/facebook as a banner ad that promotes dental health in dogs. Therefore I will need the photoshop files as well as pngs/pdfs.
I want a dog and a cat in the image used for the poster with them showing healthy teeth and looking happy!
The feels is to be professional but also cute/funny. Using the orange coming through from the logo and the logo somewhere on the poster.
The text as below
Heading: Join our Dental Evergreen Plan!
Text: Keep your fur child smiling all year round while we cap their dental work at $365 if they return for a dental clean within 365 days! The plan includes full mouth dental x-rays and scale and polish of all teeth under a carefully monitored general anaesthetic! That'll give you both a reason to smile and save you over $180 per dental! *
Conditions (in smaller writing): *Any extractions and more advanced dental procedures if required will incur an additional cost that will be discussed with your prior to the procedure.
Thanks

```html
<!DOCTYPE html>
<html lang="en">
<head>
<meta charset="utf-8">
<title>Join Our Dental Evergreen Plan – Mossgate Vets</title>
<link rel="stylesheet" href="https://fonts.googleapis.com/css2?family=League+Spartan:wght@500;700&family=Quicksand:wght@600;700&family=Lato:ital@1&display=swap">
<style>
  :root {
    --frame: #3d3d3f;
    --paper: #f4f4f5;
    --orange: #f7941d;
    --brown: #6e4b3f;
    --white: #ffffff;
    --photo-light: #e9e6e3;
    --photo-warm: #b89478;
    --photo-dark: #7a5d48;
  }
  * { box-sizing: border-box; margin: 0; padding: 0; }
  html, body { width: 875px; height: 1200px; overflow: hidden; }
  body { background: var(--frame); position: relative; }

  .poster {
    position: absolute; left: 46px; top: 46px;
    width: 783px; height: 1108px;
    background: linear-gradient(135deg, #ffffff 0%, var(--paper) 55%, #e9e9eb 100%);
    overflow: hidden;
  }

  .pet-photo {
    position: absolute; left: 10px; top: 96px;
    width: 454px; height: 940px;
    border-radius: 180px 180px 0 0;
    background:
      radial-gradient(ellipse 60% 30% at 45% 22%, var(--photo-warm) 0%, rgba(184,148,120,0) 100%),
      radial-gradient(ellipse 70% 35% at 50% 72%, #a88a6c 0%, rgba(168,138,108,0) 100%),
      linear-gradient(180deg, var(--photo-light) 0%, #d7c6b6 45%, var(--photo-dark) 100%);
  }

  .plan-banner {
    position: absolute; left: 464px; top: 0;
    width: 296px; height: 492px;
    background: var(--orange);
    clip-path: polygon(0 0, 100% 0, 100% 100%, 50% 92.7%, 0 100%);
  }
  .plan-banner__lead {
    position: absolute; top: 58px; left: 0; width: 100%;
    text-align: center; color: var(--white);
    font: 700 58px/1 "League Spartan", sans-serif; letter-spacing: -1px;
  }
  .plan-badge {
    position: absolute; left: 10px; top: 140px; width: 276px; height: 276px;
  }
  .plan-badge__title {
    position: absolute; left: 0; top: 202px; width: 100%;
    text-align: center; color: var(--brown);
    font-family: "League Spartan", sans-serif; font-weight: 700; line-height: 1;
  }
  .plan-badge__title span { display: block; }
  .plan-badge__title .word-1 { font-size: 44px; }
  .plan-badge__title .word-2 { font-size: 38px; margin-top: 6px; }
  .plan-badge__title .word-3 { font-size: 54px; margin-top: 8px; }

  .clinic-name {
    position: absolute; left: 464px; top: 560px; width: 296px;
    display: flex; align-items: center; justify-content: center; gap: 10px;
    color: var(--orange);
    font: 700 36px/1 "League Spartan", sans-serif;
  }
  .clinic-name__dot {
    width: 22px; height: 22px; border-radius: 50%; background: var(--orange);
  }

  .offer-panel {
    position: absolute; left: 464px; top: 718px;
    width: 296px; height: 318px; background: var(--orange);
  }
  .offer-callout {
    position: absolute; left: 468px; top: 686px;
    width: 288px; height: 190px;
    background: var(--orange);
    clip-path: polygon(50% 0, 100% 18%, 100% 100%, 0 100%, 0 18%);
  }
  .offer-callout__inner {
    position: absolute; left: 4px; top: 4px; right: 4px; bottom: 4px;
    background: var(--brown);
    clip-path: polygon(50% 0, 100% 18%, 100% 100%, 0 100%, 0 18%);
    display: flex; align-items: flex-end; justify-content: center;
    padding: 0 6px 10px;
    color: var(--white); text-align: center;
    font: 700 18.5px/1.27 "Quicksand", sans-serif;
  }
  .offer-details {
    position: absolute; left: 474px; top: 890px; width: 276px;
    color: var(--white); text-align: center;
    font: 700 12.8px/1.45 "Quicksand", sans-serif;
  }
  .offer-details p + p { margin-top: 13px; }

  .conditions {
    position: absolute; left: 0; top: 1036px; width: 783px; height: 72px;
    background: var(--brown); border-top: 3px solid var(--orange);
    display: flex; align-items: center; justify-content: center;
    color: var(--white); text-align: center;
    font: italic 13px/1.45 "Lato", sans-serif;
  }
</style>
</head>
<body>
<main class="poster">
  <div class="pet-photo" role="img" aria-label="Photo of a happy dog sitting behind a smiling tabby kitten, both showing healthy teeth"></div>

  <section class="plan-banner">
    <h1 class="plan-banner__lead">JOIN OUR</h1>
    <svg class="plan-badge" viewBox="0 0 276 276" aria-hidden="true">
      <g fill="none" stroke="#ffffff" stroke-width="7" stroke-linecap="round">
        <path d="M 68 36 A 130 130 0 0 1 232 46"/>
        <path d="M 266 120 A 130 130 0 0 1 180 262"/>
        <path d="M 118 267 A 130 130 0 0 1 24 80"/>
      </g>
      <g fill="#ffffff">
        <polygon points="222,30 256,70 214,66"/>
        <polygon points="250,104 276,110 264,148"/>
        <polygon points="188,246 150,272 190,282"/>
        <polygon points="8,90 40,64 46,98"/>
      </g>
    </svg>
    <h2 class="plan-badge__title">
      <span class="word-1">DENTAL</span>
      <span class="word-2">EVERGREEN</span>
      <span class="word-3">PLAN!</span>
    </h2>
  </section>

  <div class="clinic-name"><span class="clinic-name__dot"></span>Mossgate Vets</div>

  <div class="offer-panel"></div>
  <div class="offer-callout">
    <p class="offer-callout__inner">Keep your<br>fur child smiling all year<br>round while we cap their<br>dental work at $365 if<br>they return for a dental<br>clean within 365 days!</p>
  </div>
  <div class="offer-details">
    <p>The plan includes full mouth dental<br>x-rays and scale and polish of all teeth<br>under a carefully monitored general<br>anaesthetic!</p>
    <p>That'll give you both a reason to smile<br>and save you over $180 per dental!</p>
  </div>

  <footer class="conditions">
    <p>*Any extractions and more advanced dental procedures if required will incur an<br>additional cost that will be discussed with your prior to the procedure.</p>
  </footer>
</main>
</body>
</html>
```